Crest of Morning Paddocks Business Cards with logo

Need a creative business card that pops. Colorful but professional. The attached logo should be included. We are a national horse racing partnership so we are in the equine business. Nothing cartoonlike or whimsical.

Target Market(s)

professionals - 40+

Contact Information for Business Card

Maren Dunleavy
Director of Operations
27 Ashbrook Lane
Fairhaven, KY. 40584

Phone (502) 555-0147

FX: (859) 555-0192

email: maren@cmpaddocks.example
cmpaddocks.example

Requirements
Must have
• All information above should be on the business card including the website address. Professional yet creative
Nice to have
• an attention grabbing design. not boring. exciting.
Should not have
• cartoon like - whimsical.

```html
<!DOCTYPE html>
<html lang="en">
<head>
<meta charset="utf-8">
<title>Crest of Morning Paddocks — Business Card</title>
<link rel="stylesheet" href="https://fonts.googleapis.com/css2?family=Montserrat:wght@700&family=EB+Garamond:wght@400;700&display=swap">
<style>
  :root {
    --backdrop: #e4e3e8;
    --card-black: #0b0b0c;
    --card-sheen: #1c1c1f;
    --gold: #d1a83a;
    --navy: #4a4f9a;
    --ink-light: #e9e7e2;
  }
  * { box-sizing: border-box; margin: 0; padding: 0; }
  html, body {
    width: 1200px; height: 1000px; overflow: hidden;
    background: var(--backdrop);
  }
  .canvas { position: relative; width: 1200px; height: 1000px; }
  .business-card {
    position: absolute; left: 150px; top: 243px;
    width: 900px; height: 514px;
    background: linear-gradient(115deg, var(--card-black) 0%, var(--card-sheen) 55%, var(--card-black) 100%);
    border-radius: 6px;
    box-shadow: 0 18px 40px rgba(0,0,0,0.25);
    overflow: hidden;
    font-family: "EB Garamond", Georgia, serif;
    color: var(--ink-light);
  }
  .accent-band { position: absolute; left: 0; top: 0; }
  .brand-mark {
    position: absolute; left: 60px; top: 120px;
    display: flex; align-items: center; gap: 14px;
  }
  .brand-mark__dot {
    width: 26px; height: 26px; border-radius: 50%;
    background: var(--gold); flex: none;
  }
  .brand-mark__name {
    font-weight: 700; font-size: 30px; line-height: 1.05;
    color: var(--navy); width: 220px;
  }
  .holder { position: absolute; right: 60px; top: 62px; text-align: right; }
  .holder__name {
    font-family: "Montserrat", Arial, sans-serif;
    font-weight: 700; font-size: 40px; letter-spacing: 0.5px;
    color: var(--gold); line-height: 1;
  }
  .holder__title { font-size: 22px; margin-top: 4px; }
  .address {
    position: absolute; right: 60px; top: 250px; text-align: right;
    font-style: normal; font-size: 25px; line-height: 1.3;
  }
  .address__web { color: var(--gold); font-weight: 700; }
  .contact {
    position: absolute; left: 60px; top: 392px;
    list-style: none; font-size: 25px; line-height: 1.3;
  }
  .contact__label {
    color: var(--gold); font-weight: 700; display: inline-block; width: 24px;
  }
</style>
</head>
<body>
<main class="canvas">
  <section class="business-card" aria-label="Business card for Maren Dunleavy">
    <svg class="accent-band" width="900" height="514" viewBox="0 0 900 514" role="img" aria-label="Diagonal striped band in navy and gold">
      <defs>
        <linearGradient id="bandTone" x1="0" y1="0" x2="1" y2="0">
          <stop offset="0" stop-color="#4a4f9a"/>
          <stop offset="0.5" stop-color="#8c7d6a"/>
          <stop offset="1" stop-color="#d1a83a"/>
        </linearGradient>
      </defs>
      <line x1="60" y1="378" x2="860" y2="178" stroke="url(#bandTone)" stroke-width="11"/>
    </svg>

    <div class="brand-mark">
      <span class="brand-mark__dot"></span>
      <span class="brand-mark__name">Crest of Morning Paddocks</span>
    </div>

    <header class="holder">
      <h1 class="holder__name">MAREN DUNLEAVY</h1>
      <p class="holder__title">Director Of Operations</p>
    </header>

    <address class="address">
      27 Ashbrook Lane<br>
      Fairhaven, KY. 40584<br>
      <span class="address__web">www.cmpaddocks.example</span>
    </address>

    <ul class="contact">
      <li><span class="contact__label">P</span>(502) 555-0147</li>
      <li><span class="contact__label">F</span>(859) 555-0192</li>
      <li><span class="contact__label">E</span>maren@cmpaddocks.example</li>
    </ul>
  </section>
</main>
</body>
</html>
```